Bright Anchor Tools and Building Supply Inc. (Rebranding)

Target Market(s)

mainly people who do DIY, and also construction companies.

Industry/Entity Type

Construction

Contact Information for Business Card

418 R. Velasco St. Brgy. 164 Sta. Lucia Manila, Philippines 1003
(02) 861-4097
www.bat.example
brightanchortools@mailbox.example

Number of Pages Required

5+ page

Font styles to use
Sans Serif

Colors
f37122
f78f20

Requirements
Must have
• to RETAIN the current logo used.
Nice to have
• ideas on how to apply the current logos to different promotional items
Should not have
• DO NOT change the Current Logo

```html
<!DOCTYPE html>
<html lang="en">
<head>
<meta charset="utf-8">
<title>Bright Anchor Tools and Building Supply Inc. – Business Card</title>
<link rel="stylesheet" href="https://fonts.googleapis.com/css2?family=Montserrat:wght@400;500;800&display=swap">
<style>
  :root {
    --backdrop: #e6e6e6;
    --card-white: #ffffff;
    --brand-orange: #fd5d1f;
    --accent-grey: #9e9e9e;
    --text-grey: #7a7a7a;
    --divider: #d8d8d8;
  }
  * { margin: 0; padding: 0; box-sizing: border-box; }
  html, body {
    width: 1200px; height: 1000px; overflow: hidden;
    background: var(--backdrop);
    font-family: "Montserrat", Arial, sans-serif;
  }
  .canvas { position: relative; width: 1200px; height: 1000px; }
  .card {
    position: absolute; top: 371px; width: 421px; height: 257px; overflow: hidden;
  }
  .card--front { left: 168px; background: var(--card-white); }
  .card--back { left: 611px; background: var(--brand-orange); }

  .brand {
    position: absolute; display: flex; align-items: center; gap: 10px;
    font-weight: 800; text-transform: uppercase; line-height: 1.1;
  }
  .brand__mark { width: 18px; height: 18px; border-radius: 50%; flex: none; }
  .brand__name { font-size: 19px; letter-spacing: 0.5px; }
  .card--front .brand { left: 50%; top: 48px; transform: translateX(-50%); color: var(--brand-orange); }
  .card--front .brand__mark { background: var(--brand-orange); }
  .card--back .brand { left: 50%; top: 90px; transform: translateX(-50%); color: var(--card-white); }
  .card--back .brand__mark { background: var(--card-white); }

  .holder {
    position: absolute; right: 220px; top: 161px; text-align: right; color: var(--text-grey);
  }
  .holder__name { font-size: 17px; font-weight: 400; color: var(--brand-orange); line-height: 1; }
  .holder__role { font-size: 9.5px; line-height: 1.2; }
  .holder__address { font-size: 9px; line-height: 1.3; margin-top: 4px; }

  .divider {
    position: absolute; left: 211px; top: 154px; width: 1px; height: 70px; background: var(--divider);
  }
  .contacts {
    position: absolute; left: 220px; top: 163px; list-style: none;
    font-size: 8.5px; color: var(--text-grey); line-height: 13px;
  }
  .contacts__label { color: var(--brand-orange); font-weight: 500; }

  .card__bands { position: absolute; left: 0; bottom: 0; width: 421px; height: 26px; }
</style>
</head>
<body>
<main class="canvas">
  <section class="card card--front" aria-label="Business card front">
    <div class="brand">
      <span class="brand__mark"></span>
      <span class="brand__name">Bright Anchor Tools and<br>Building Supply Inc.</span>
    </div>

    <div class="holder">
      <p class="holder__name">Your Name</p>
      <p class="holder__role">Manager</p>
      <p class="holder__address">418 R. Velasco St.<br>Sta. Lucia</p>
    </div>
    <div class="divider"></div>
    <ul class="contacts">
      <li><span class="contacts__label">P</span> : (02) 861-4097</li>
      <li><span class="contacts__label">C</span> : (02) 861-4097</li>
      <li><span class="contacts__label">F</span> : (02) 861-4097</li>
      <li><span class="contacts__label">E</span> : brightanchortools@mailbox.example</li>
    </ul>

    <svg class="card__bands" viewBox="0 0 421 26" aria-hidden="true">
      <polygon points="0,6 242,6 224,26 0,26" fill="var(--brand-orange)"/>
      <polygon points="260,0 421,0 421,26 236,26" fill="var(--accent-grey)"/>
    </svg>
  </section>

  <section class="card card--back" aria-label="Business card back">
    <div class="brand">
      <span class="brand__mark"></span>
      <span class="brand__name">Bright Anchor Tools and<br>Building Supply Inc.</span>
    </div>
  </section>
</main>
</body>
</html>
```